An organic baby/mommy skin care product company needs a web design

We need a web design for an organic baby and mommy skin care product company based in NY/NJ called "Lumo & Pinnet". We have developed a half dozen of all natural, organic baby/mommy skin care products that apply on different part of body. For instance, baby bottom balm/cream/oil to effectively cure/prevent diaper rash etc.

The design is for main/intro page, product page and shipping/packaging page.The theme/template will be uploaded to a CartVeldo 1.4.7.3 enviroment (also looking for alternative solutions).
Updates

Target Market(s)

Young professional parents, educated stay-home moms, caring grandparents.

Industry/Entity Type

Skin Care Product

Requirements
Must have
• Logo on upper left; slideshow pictures (up to 5) on main page;
Nice to have
• Cute background picture (a boy and a girl, etc) font, colors.
Should not have
• Please do not try to list all/most products on the main page. 2 to 3 feature products from each category should be enough.

```html
<!DOCTYPE html>
<html lang="en">
<head>
<meta charset="utf-8">
<title>Lumo &amp; Pinnet – Organic Baby &amp; Mommy Skin Care</title>
<link rel="stylesheet" href="https://fonts.googleapis.com/css2?family=Arimo:wght@400;700&family=Cabin:wght@400;500&display=swap">
<style>
:root{
  --bar-top:#242424;
  --bar-bottom:#050505;
  --page-dark:#141414;
  --panel:#f7f7f7;
  --card:#d4d4d4;
  --purple:#8f5cb8;
  --purple-light:#b48ad6;
  --purple-text:#8d4fb8;
  --text:#222;
  --muted:#666;
  --white:#fff;
}
*{box-sizing:border-box;margin:0;padding:0}
html,body{width:1200px;height:1169px;overflow:hidden}
body{position:relative;background:var(--page-dark);font-family:"Arimo",Arial,sans-serif;color:var(--text)}
.abs{position:absolute}

/* top bar */
.topbar{left:0;top:0;width:1200px;height:58px;background:linear-gradient(var(--bar-top) 0 29px,var(--bar-bottom) 29px)}
.logo{left:136px;top:21px;color:var(--white);font:700 13px "Arimo",sans-serif;letter-spacing:-.8px}
.toplinks{right:94px;font:400 12.5px "Cabin",sans-serif;color:#eee;display:flex;white-space:nowrap}
.toplinks span{padding:0 7px;border-left:1px solid #444}
.toplinks span.nb{border-left:0}
.row1{top:11px}
.row2{top:32px;right:92px}

/* hero */
.hero{left:0;top:58px;width:1200px;height:731px;
  background:radial-gradient(ellipse 420px 330px at 600px 300px,#f4d9c8 0,#f0d4c2 55%,rgba(240,212,194,0) 100%),
  linear-gradient(90deg,#eef1f6 0,#f6f3f1 30%,#f6f3f1 70%,#e9eef6 100%)}

/* nav */
.nav{left:105px;top:440px;width:991px;height:55px;background:linear-gradient(#262626 0 28px,#050505 28px)}
.nav a{position:absolute;top:19px;font:700 16px "Arimo",sans-serif;letter-spacing:-1px;color:var(--purple-light);text-decoration:none}
.nav a.active{color:var(--white)}
.search{left:641px;top:15px;width:302px;height:24px;background:#eee;border:1px solid #ccc;font:italic 15px "Arimo",sans-serif;color:#999;padding:3px 6px}
.go{left:942px;top:15px;width:36px;height:24px;background:var(--purple);color:var(--white);font:500 15px "Cabin",sans-serif;text-align:center;line-height:24px}

.content{left:105px;top:495px;width:991px;height:573px;background:var(--panel)}

/* product cards */
.card{width:271px;height:220px;top:532px;background:var(--card)}
.card .img{position:absolute;left:5px;top:5px;width:260px;height:155px;background:radial-gradient(ellipse at center,#dfe3f1 0,#fff 70%)}
.card h3{position:absolute;left:5px;top:166px;font:400 16px "Cabin",sans-serif;letter-spacing:.6px;color:#222;word-spacing:4px}
.card p{position:absolute;left:5px;top:186px;width:150px;font:400 12px "Arimo",sans-serif;line-height:13px;color:var(--muted);word-spacing:4px}
.btn{position:absolute;background:var(--purple);color:var(--white);font:400 15px "Cabin",sans-serif;text-align:center}
.card .btn{left:212px;top:188px;width:53px;height:25px;line-height:25px}

.arrow{top:596px}

/* updates */
.updates{left:187px;top:800px;width:550px;height:228px;background:var(--white);border:3px solid #222;border-top:0}
.box-head{height:28px;background:linear-gradient(#333 0 14px,#1c1c1c 14px);color:var(--white);font:400 16px "Cabin",sans-serif;padding:5px 1px}
.item{margin:6px 6px 0 7px;background:#e8e8e8;padding:6px 6px 5px}
.item h4{font:400 13px "Arimo",sans-serif;color:var(--purple-text)}
.item time{display:block;font:400 11px "Arimo",sans-serif;color:#222;margin-bottom:6px}
.item p{font:400 11.3px/15px "Arimo",sans-serif;color:#333;white-space:nowrap}

/* contact */
.contact{left:747px;top:800px;width:274px;height:228px;background:var(--white);border:4px solid #555;border-top:0}
.contact .box-head{background:linear-gradient(#666 0 14px,#555 14px);margin:0 -4px;padding-left:4px}
.contact label{position:absolute;right:218px;font:400 15px "Cabin",sans-serif;color:#222}
.field{position:absolute;left:56px;width:200px;background:#fafafa;border:1px solid #e4e4e4;box-shadow:inset 0 2px 3px #ddd}
.contact .btn{left:203px;top:193px;width:53px;height:24px;line-height:24px}

/* footer */
.footer{left:105px;top:1068px;width:991px;height:101px;background:linear-gradient(#222 0 52px,#050505 52px)}
.copy{left:30px;top:44px;font:400 14px "Arimo",sans-serif;color:#555}
</style>
</head>
<body>

<header class="abs topbar">
  <div class="abs logo">YOUR LOGO HERE</div>
  <nav class="abs toplinks row1"><span class="nb">24x7 Customer Support &nbsp;-&nbsp; Contact Us</span><span>Home</span><span>Account</span><span>Wishlist</span><span style="margin-left:4px">Login</span><span>Signup</span></nav>
  <nav class="abs toplinks row2"><span class="nb">e-Gift Voucher</span><span class="nb" style="margin-left:5px">Wallet</span><span class="nb" style="margin-left:2px">Digital Cart (0)</span></nav>
</header>

<div class="abs hero" role="img" aria-label="Slideshow photo: close-up of a baby wearing a soft white hat with blue stars and moons"></div>

<nav class="abs nav">
  <a class="active" style="left:37px">HOME</a>
  <a style="left:122px">COMPANY</a>
  <a style="left:237px">PRODUCTS</a>
  <a style="left:360px">CONTACT US</a>
  <div class="abs search">search</div>
  <div class="abs go">Go</div>
</nav>

<main class="abs content"></main>

<svg class="abs arrow" style="left:135px" width="42" height="82" viewBox="0 0 42 82"><polyline points="38,3 5,41 38,79" fill="none" stroke="#8f5cb8" stroke-width="7"/></svg>
<svg class="abs arrow" style="left:1031px" width="42" height="82" viewBox="0 0 42 82"><polyline points="4,3 37,41 4,79" fill="none" stroke="#8f5cb8" stroke-width="7"/></svg>

<article class="abs card" style="left:186px">
  <div class="img" role="img" aria-label="Product photo: baby lotion bottles and tubes"></div>
  <h3>Product ID 07AC</h3><p>Breif description of the product here</p><span class="btn">more</span>
</article>
<article class="abs card" style="left:468px">
  <div class="img" role="img" aria-label="Product photo: gift pouch with balms and oil bottles" style="background:radial-gradient(ellipse at center,#f3e6c2 0,#fff 70%)"></div>
  <h3>Product ID 07AC</h3><p>Breif description of the product here</p><span class="btn">more</span>
</article>
<article class="abs card" style="left:750px">
  <div class="img" role="img" aria-label="Product photo: jar of hydrating cream" style="background:radial-gradient(ellipse 70px 70px at center,#a79ad8 0,#d9d4ef 60%,#fff 100%)"></div>
  <h3>Product ID 07AC</h3><p>Breif description of the product here</p><span class="btn">more</span>
</article>

<section class="abs updates">
  <div class="box-head">Latest Updates</div>
  <div class="item"><h4>Huge discount offer</h4><time>August 15, 2012</time>
    <p>This is Sketchwell's version &nbsp;of Lorem Ipsum. Proin gravida nibh vel velit auctor aliquet. Aenean<br>sollicitudin, lorem quis bibendum auctor, nisi elit consequat ipsum, nec sagittis sem nibh id elit.<br>Duis sed odio sit amet nibh vulputate cursus a sit amet mauris. Morbi accumsan ipsum velit. Nam</p></div>
  <div class="item"><h4>Huge discount offer</h4><time>August 15, 2012</time>
    <p>This is Sketchwell's version &nbsp;of Lorem Ipsum. Proin gravida nibh vel velit auctor aliquet. Aenean<br>sollicitudin, lorem quis bibendum auctor, nisi elit consequat ipsum, nec sagittis sem nibh id elit.<br>Duis sed odio sit amet nibh vulputate cursus a sit amet mauris. Morbi accumsan ipsum velit. Nam</p></div>
</section>

<section class="abs contact">
  <div class="box-head">Contact Us</div>
  <label style="top:38px">Name</label><div class="field" style="top:38px;height:18px"></div>
  <label style="top:61px">Email</label><div class="field" style="top:61px;height:18px"></div>
  <label style="top:84px">Text</label><div class="field" style="top:84px;height:78px"></div>
  <label style="top:165px">Code</label><div class="field" style="top:166px;height:18px"></div>
  <span class="btn">send</span>
</section>

<footer class="abs footer"><div class="abs copy">Copyrights reserved 2012</div></footer>

</body>
</html>
```